Construction company yard sign

I would like a design for yard signs for my construction company. It will be used to put outside clients homes as we are working for them and will be used as advertisement for neighbors that are passing by the home.

The sign will be 18x24 and a plastic type material.

Target Market(s)

Homeowners

Font styles to use
Sans Serif

Requirements
Must have
• The most important thing about the sign is the visibility of the lettering and phone number 520-555-0147. The next would be Free roof Inspections. and then I would like to have these 3 words on there as well: Flat - Shingle - Tile

```html
<!DOCTYPE html>
<html lang="en">
<head>
<meta charset="utf-8">
<title>Halvorsen Construction Group – Yard Sign</title>
<link href="https://fonts.googleapis.com/css2?family=Montserrat:wght@800&display=swap" rel="stylesheet">
<style>
  :root {
    --red: #ec2329;
    --blue: #35a8d8;
    --blue-mid: #1c8ac0;
    --blue-deep: #146a90;
    --white: #ffffff;
    --backdrop: #d9d9d9;
    --photo-sky: #f4f2f0;
    --photo-roof: #3d4a66;
    --photo-wall: #8d8f9e;
    --photo-lawn: #6f7f54;
  }
  * { margin: 0; padding: 0; box-sizing: border-box; }
  html, body {
    width: 974px; height: 1200px; overflow: hidden;
    background: var(--backdrop);
    font-family: "Montserrat", sans-serif;
    font-weight: 800;
  }
  .sign {
    position: absolute; left: 37px; top: 0;
    width: 900px; height: 1200px;
    background: var(--white);
    overflow: hidden;
  }
  .corner-block {
    position: absolute; top: 0; width: 170px; height: 174px;
    background: var(--red);
  }
  .corner-block.left { left: 0; }
  .corner-block.right { right: 0; }
  .brand {
    position: absolute; left: 212px; top: 56px; width: 484px; height: 104px;
    display: flex; align-items: center; gap: 16px;
    color: var(--blue);
  }
  .brand-square {
    width: 78px; height: 78px; flex: none;
    background: var(--blue);
  }
  .brand-name { line-height: 1; }
  .brand-name .line-main { display: block; font-size: 54px; letter-spacing: 1px; }
  .brand-name .line-sub { display: block; font-size: 17.5px; letter-spacing: 4.2px; margin-top: 8px; }
  .headline-free {
    position: absolute; left: 0; right: 0; top: 188px;
    text-align: center;
    font-size: 247px; line-height: 1;
    letter-spacing: -4px;
    color: var(--blue);
  }
  .headline-service {
    position: absolute; left: 0; right: 0; top: 400px;
    text-align: center;
    font-size: 62px; line-height: 1;
    letter-spacing: -1px;
    color: var(--red);
  }
  .house-photo {
    position: absolute; left: 0; top: 560px; width: 900px; height: 424px;
    background: linear-gradient(180deg, var(--photo-sky) 0%, var(--photo-roof) 28%, var(--photo-wall) 62%, var(--photo-lawn) 100%);
  }
  .roof-types {
    position: absolute; left: 0; top: 984px; width: 900px; height: 82px;
    display: flex;
  }
  .roof-type {
    display: flex; align-items: center; justify-content: center;
    color: var(--white); font-size: 52px; letter-spacing: -0.5px;
  }
  .roof-type.flat { width: 259px; background: var(--blue); }
  .roof-type.shingle { width: 378px; background: var(--blue-mid); }
  .roof-type.tile { width: 263px; background: var(--blue-deep); }
  .phone-band {
    position: absolute; left: 0; top: 1066px; width: 900px; height: 134px;
    background: var(--red);
    display: flex; align-items: center; justify-content: center;
  }
  .phone-number {
    color: var(--white); font-size: 116px; line-height: 1;
    letter-spacing: -3px; white-space: nowrap;
  }
</style>
</head>
<body>
  <main class="sign">
    <div class="corner-block left"></div>
    <div class="corner-block right"></div>

    <header class="brand">
      <span class="brand-square"></span>
      <span class="brand-name">
        <span class="line-main">HALVORSEN</span>
        <span class="line-sub">CONSTRUCTION GROUP</span>
      </span>
    </header>

    <h1 class="headline-free">FREE</h1>
    <h2 class="headline-service">ROOF INSPECTIONS</h2>

    <div class="house-photo" role="img" aria-label="Photo of a two-storey suburban house with dark shingle roof, grey siding, lit windows, a double garage and a wet driveway at dusk"></div>

    <section class="roof-types">
      <div class="roof-type flat">FLAT</div>
      <div class="roof-type shingle">SHINGLE</div>
      <div class="roof-type tile">TILE</div>
    </section>

    <footer class="phone-band">
      <span class="phone-number">520-555-0147</span>
    </footer>
  </main>
</body>
</html>
```